Tovin Marsk Technologies Web Site

I need website designed for Tovin Marsk Technologies, LLC. It is an email marketing software as a service business. I am looking for a five page website with the ability to accept payments. I have included our logo below for integration with the website. I do not have the text ready yet.

The domain to use is tovin-marsk.com

I have also included some examples of other websites that outline the basic structure I would like
https://trybluvesto.com/
https://www.postvaro.com/

I know I need to provide some more information, but I want to get the ball rolling and see what is needed.
Thanks!
Eli

```html
<!DOCTYPE html>
<html lang="en">
<head>
<meta charset="utf-8">
<title>Tovin Marsk Technologies — Email Marketing Software</title>
<link rel="stylesheet" href="https://fonts.googleapis.com/css2?family=Nunito+Sans:ital,wght@0,400;0,600;0,700;0,800;1,400&display=swap">
<style>
:root{
  --navy:#1f2163;
  --indigo:#2e2c7e;
  --indigo-2:#3f3a96;
  --teal:#2fb0c9;
  --teal-btn:#28aec6;
  --blue:#3a80d2;
  --red:#e3101e;
  --grey:#6b6b70;
  --grey-light:#9a9aa0;
  --ink:#333338;
  --line:#d9d9de;
  --white:#ffffff;
  --violet-text:#5b4e9e;
}
*{margin:0;padding:0;box-sizing:border-box}
html,body{width:1200px;height:3103px;overflow:hidden}
body{position:relative;font-family:"Nunito Sans",Arial,sans-serif;color:var(--ink);background:var(--white)}
.abs{position:absolute}
a{color:inherit;text-decoration:none}

/* header / hero */
.hero-bg{left:0;top:0;width:1200px;height:600px;overflow:hidden;background:linear-gradient(180deg,#f1f1f3 0%,#fafafa 100%)}
.hero-circle{left:527px;top:-321px;width:952px;height:952px;border-radius:50%;background:linear-gradient(200deg,var(--indigo-2),var(--indigo) 60%,#252366)}
.brand{left:182px;top:14px;width:180px;text-align:center}
.brand-mark{width:78px;height:78px;border-radius:50%;border:3px solid var(--teal);margin:0 auto 8px}
.brand-name{font-size:19px;font-weight:600;color:var(--indigo);letter-spacing:1px;line-height:1.15}
.auth{top:27px;height:29px;font-size:13px;display:flex;align-items:center;justify-content:center;color:var(--white)}
.auth.login{left:830px;width:91px;border:1.5px solid var(--white);background:transparent}
.auth.signup{left:927px;width:93px;background:var(--teal)}
.nav{font-size:17px;color:var(--white)}
.nav a{position:absolute;white-space:nowrap}
.laptop{left:542px;top:197px;width:503px;height:358px;border-radius:10px 10px 14px 14px;background:linear-gradient(180deg,#4d4f55 0%,#bfc0c4 35%,#e4e5e8 100%)}
.hero-title{left:182px;top:234px;font-size:34px;line-height:43px;font-weight:700;color:var(--navy);letter-spacing:0.2px}
.hero-title .accent{color:var(--teal)}
.hero-text{left:182px;top:381px;width:340px;font-size:17px;line-height:21px;color:var(--violet-text)}
.btn-red{left:182px;top:463px;width:182px;height:48px;background:var(--red);color:var(--white);font-size:18px;font-weight:700;display:flex;align-items:center;justify-content:center}
.arrow{width:30px;height:56px}

/* brands */
.trusted{top:610px;left:0;width:1200px;text-align:center;font-size:16px;font-weight:600;color:var(--grey);letter-spacing:0.5px}
.brands{top:666px;left:170px;width:860px;display:flex;justify-content:space-between;align-items:center;font-size:24px;font-weight:700;color:#9b9ba2}
.divider{left:170px;top:745px;width:838px;height:1px;background:var(--line)}

/* about */
.about-title{top:796px;left:0;width:1200px;text-align:center;font-size:35px;font-weight:700;color:var(--navy)}
.about-text{top:851px;left:180px;width:840px;text-align:center;font-size:20px;line-height:28px;color:var(--grey)}

/* blue band */
.band{left:0;top:1190px;width:1200px;height:699px}
.card{top:981px;width:256px;height:329px;background:var(--white);border-radius:8px;box-shadow:0 4px 18px rgba(30,40,90,.16);text-align:center}
.card-icon{width:104px;height:104px;margin:18px auto 0;border-radius:50%;background:#f1f2f6;display:flex;align-items:center;justify-content:center}
.card-title{margin-top:30px;font-size:19px;font-weight:700;color:var(--navy)}
.card-text{margin:14px auto 0;width:200px;font-size:13px;line-height:20px;color:var(--ink)}
.card-btn{margin:14px auto 0;width:150px;height:42px;background:var(--teal-btn);color:var(--white);font-size:15px;font-weight:700;display:flex;align-items:center;justify-content:center}
.services-title{top:1360px;left:0;width:1200px;text-align:center;font-size:30px;font-weight:600;color:var(--white)}
.service{width:420px}
.service svg{position:absolute;left:0;top:0}
.service-title{position:absolute;left:72px;top:0;font-size:22px;font-weight:700;color:var(--white);white-space:nowrap}
.service-text{position:absolute;left:72px;top:36px;width:340px;font-size:14px;line-height:22px;color:rgba(255,255,255,.62)}

/* testimonials */
.testi-title{top:1948px;left:0;width:1200px;text-align:center;font-size:30px;font-weight:600;color:#5f5f66}
.testi-shadow{left:306px;top:2080px;width:558px;height:190px;background:#8fd3e6}
.testi-card{left:315px;top:2067px;width:558px;height:194px;background:var(--white);border:1px solid #cfd2d8}
.avatar{left:552px;top:2021px;width:96px;height:96px;border-radius:50%;background:linear-gradient(180deg,#c9cdd3,#6d727a)}
.quote{left:375px;top:2125px;width:450px;text-align:center;font-size:12.5px;line-height:21px;font-style:italic;color:#6f6f78}
.qmark{font-size:54px;font-weight:800;color:var(--blue);line-height:1}
.author{left:315px;top:2205px;width:558px;text-align:center;font-size:14px;font-weight:600;color:#444}

/* call to action */
.cta{left:0;top:2375px;width:1200px;height:381px;background:linear-gradient(100deg,#2a2668 0%,#3b3482 50%,#2c2a6c 100%)}
.cta-title{top:2458px;left:0;width:1200px;text-align:center;font-size:29px;font-weight:700;color:var(--white);letter-spacing:.5px}
.cta-sub{top:2496px;left:0;width:1200px;text-align:center;font-size:23px;font-weight:700;color:var(--white)}
.cta-text{top:2543px;left:0;width:1200px;text-align:center;font-size:15.5px;line-height:25px;color:#e6e6f2}
.cta-btn{left:521px;top:2615px;width:151px;height:40px;background:var(--teal-btn);color:var(--white);font-size:15px;font-weight:700;display:flex;align-items:center;justify-content:center}

/* footer */
.foot-brand{left:182px;top:2805px;width:212px;text-align:center}
.foot-col{top:2815px}
.foot-col h4{font-size:19px;font-weight:400;color:#444;margin-bottom:14px}
.foot-col li{list-style:none;font-size:14px;line-height:24px;color:var(--grey-light)}
.foot-line{left:50px;top:3035px;width:1100px;height:1px;background:#ececef}
.copy{top:3054px;left:0;width:1200px;text-align:center;font-size:11px;color:#777}
</style>
</head>
<body>

<!-- hero -->
<div class="abs hero-bg">
  <div class="abs hero-circle"></div>
</div>

<div class="abs brand">
  <div class="brand-mark"></div>
  <div class="brand-name">TOVIN MARSK<br>TECHNOLOGIES</div>
</div>

<a class="abs auth login" href="#">Log In</a>
<a class="abs auth signup" href="#">Sign Up</a>
<nav class="abs nav" style="left:0;top:72px;width:1200px;height:24px">
  <a href="#" style="left:596px">About Us</a>
  <a href="#" style="left:695px">Services</a>
  <a href="#" style="left:788px">Solution</a>
  <a href="#" style="left:879px">Pricing</a>
  <a href="#" style="left:958px">Contact</a>
</nav>

<div class="abs laptop" role="img" aria-label="Photo of an open laptop showing an email dashboard"></div>

<h1 class="abs hero-title"><span class="accent">EMAIL MARKETING</span><br>SOFTWARE AND<br>TECHNOLOGY</h1>
<p class="abs hero-text">Class aptent taciti sociosqu ad litora torquent per conubia nostra per inceptos hymenaeos Proin nulla arcu</p>
<a class="abs btn-red" href="#">Get Started</a>

<svg class="abs arrow" style="left:94px;top:324px" viewBox="0 0 30 56"><polyline points="26,2 4,28 26,54" fill="none" stroke="#8d8d95" stroke-width="2.5"/></svg>
<svg class="abs arrow" style="left:1090px;top:324px" viewBox="0 0 30 56"><polyline points="4,2 26,28 4,54" fill="none" stroke="#ffffff" stroke-width="2.5"/></svg>

<!-- trusted by -->
<div class="abs trusted">TRUSTED BY BRANDS</div>
<div class="abs brands">
  <span>Floravia</span>
  <span>Corvane Utilities</span>
  <span>Bexmoor</span>
  <span>Quelto</span>
  <span>Drenwick</span>
</div>
<div class="abs divider"></div>

<!-- about -->
<h2 class="abs about-title">ABOUT TOVIN MARSK</h2>
<p class="abs about-text">Morbi porta libero id ullamcorper nonummy nibh ligula pulvinar metus eget consectetuer augue nisi quis lacus Ut ac mi quis lacus mollis aliquam vvs</p>

<!-- blue band -->
<svg class="abs band" viewBox="0 0 1200 699" preserveAspectRatio="none">
  <defs>
    <linearGradient id="bandGrad" x1="0" y1="0" x2="0" y2="1">
      <stop offset="0" stop-color="#3a7ed2"/>
      <stop offset="1" stop-color="#30b3c9"/>
    </linearGradient>
  </defs>
  <path d="M0,20 Q600,95 1200,5 L1200,699 L0,699 Z" fill="url(#bandGrad)"/>
</svg>

<div class="abs card" style="left:166px">
  <div class="card-icon">
    <svg width="56" height="56" viewBox="0 0 56 56" fill="none" stroke="#1f2163" stroke-width="2.2"><path d="M30 6 L50 6 L50 26 L24 52 L4 32 Z"/><circle cx="41" cy="15" r="3.5"/><path d="M20 36 L34 22"/></svg>
  </div>
  <div class="card-title">Affordable pricing</div>
  <p class="card-text">Class aptent taciti sociosqu ad litora torquent per conubia nostra per inceptos hymenaeos</p>
  <a class="card-btn" href="#">Learn More</a>
</div>
<div class="abs card" style="left:455px">
  <div class="card-icon">
    <svg width="56" height="56" viewBox="0 0 56 56" fill="none" stroke="#1f2163" stroke-width="2.2"><path d="M10 46 L36 20 a10 10 0 1 1 6 6 L16 52 Z"/><path d="M46 46 L22 22 L14 22 L8 12 L12 8 L22 14 L22 22"/></svg>
  </div>
  <div class="card-title">24/7 Support</div>
  <p class="card-text">Class aptent taciti sociosqu ad litora torquent per conubia nostra per inceptos hymenaeos</p>
  <a class="card-btn" href="#">Learn More</a>
</div>
<div class="abs card" style="left:745px">
  <div class="card-icon">
    <svg width="56" height="56" viewBox="0 0 56 56" fill="none" stroke="#1f2163" stroke-width="2.2"><rect x="6" y="8" width="44" height="34" rx="2"/><path d="M6 16 H50 M14 24 H34 M14 30 H28"/><circle cx="40" cy="40" r="8"/><circle cx="40" cy="40" r="3"/></svg>
  </div>
  <div class="card-title">Best Software</div>
  <p class="card-text">Class aptent taciti sociosqu ad litora torquent per conubia nostra per inceptos hymenaeos</p>
  <a class="card-btn" href="#">Learn More</a>
</div>

<h2 class="abs services-title">OUR SERVICES</h2>

<div class="abs service" style="left:165px;top:1500px">
  <svg width="58" height="58" viewBox="0 0 58 58" fill="none" stroke="#fff" stroke-width="2"><rect x="2" y="4" width="54" height="38"/><path d="M22 50 H36 M29 42 V50 M12 34 V26 M20 34 V20 M28 34 V24 M36 34 V14 M44 34 V18"/></svg>
  <div class="service-title">Analytics</div>
  <p class="service-text">Proin nulla arcu nonummy luctus dictum eget fermentum et lorem Class aptent taciti sociosqu d litora torquent per conubia nostra</p>
</div>
<div class="abs service" style="left:634px;top:1504px">
  <svg width="64" height="52" viewBox="0 0 64 52" fill="none" stroke="#fff" stroke-width="2"><rect x="2" y="2" width="12" height="12"/><rect x="2" y="20" width="12" height="12"/><rect x="2" y="38" width="12" height="12"/><rect x="20" y="2" width="42" height="12"/><rect x="20" y="20" width="42" height="12"/><rect x="20" y="38" width="42" height="12"/></svg>
  <div class="service-title" style="left:84px">Building Email List</div>
  <p class="service-text" style="left:84px">Proin nulla arcu nonummy luctus dictum eget fermentum et lorem Class aptent taciti sociosqu ad litora torquent per conubia nostra</p>
</div>
<div class="abs service" style="left:170px;top:1684px">
  <svg width="58" height="56" viewBox="0 0 58 56" fill="none" stroke="#fff" stroke-width="2"><rect x="4" y="2" width="48" height="30"/><path d="M4 2 L28 20 L52 2"/><rect x="10" y="36" width="46" height="8"/><rect x="10" y="46" width="46" height="8"/><path d="M48 40 h2 M48 50 h2"/></svg>
  <div class="service-title">Email Server Integration</div>
  <p class="service-text">Proin nulla arcu nonummy luctus dictum eget fermentum et lorem Class aptent taciti sociosqu ad litora torquent per conubia nostra</p>
</div>
<div class="abs service" style="left:638px;top:1688px">
  <svg width="60" height="58" viewBox="0 0 60 58" fill="none" stroke="#fff" stroke-width="2"><rect x="2" y="2" width="56" height="50"/><path d="M2 10 H58 M10 18 L34 44 M10 26 H20 M38 20 H52 M38 28 H52 M38 36 H52"/></svg>
  <div class="service-title" style="left:84px">Content Management</div>
  <p class="service-text" style="left:84px">Proin nulla arcu nonummy luctus dictum eget fermentum et lorem Class aptent taciti sociosqu ad litora torquent per conubia nostra</p>
</div>

<!-- testimonials -->
<h2 class="abs testi-title">TESTIMONIALS</h2>
<div class="abs testi-shadow"></div>
<div class="abs testi-card"></div>
<div class="abs avatar" role="img" aria-label="Portrait photo of the reviewer"></div>
<div class="abs qmark" style="left:348px;top:2108px">&ldquo;</div>
<p class="abs quote">Allamcorper est eget tempor cursus neque mi consectetuer mi a ultricies massa est sed nisl Class aptent taciti sociosqu ad litora torquent per conubia nostra per inceptos hymenaeos Proin</p>
<div class="abs qmark" style="left:742px;top:2166px">&rdquo;</div>
<div class="abs author">BY Author Name</div>
<svg class="abs arrow" style="left:133px;top:2138px" viewBox="0 0 30 56"><polyline points="26,2 4,28 26,54" fill="none" stroke="#6a6a72" stroke-width="2.5"/></svg>
<svg class="abs arrow" style="left:1020px;top:2138px" viewBox="0 0 30 56"><polyline points="4,2 26,28 4,54" fill="none" stroke="#6a6a72" stroke-width="2.5"/></svg>

<!-- call to action -->
<div class="abs cta" role="img" aria-label="Photo of people working at laptops in a dim office, tinted deep indigo"></div>
<h2 class="abs cta-title">PELLENTESQUE FAUCIBUS UT ACCUMSAN</h2>
<div class="abs cta-sub">ULTRICIES ELIT MAECENAS AT JUSTO</div>
<p class="abs cta-text">Class aptent taciti sociosqu ad litora torquent per conubia nostra per inceptos hymenaeos<br>Proin nulla arcu nonummy luctus dictum eget fermentum et lorem</p>
<a class="abs cta-btn" href="#">Click here</a>

<!-- footer -->
<div class="abs foot-brand">
  <div class="brand-mark" style="width:90px;height:90px;margin-bottom:10px"></div>
  <div class="brand-name" style="font-size:20px">TOVIN MARSK<br>TECHNOLOGIES</div>
</div>
<div class="abs foot-col" style="left:478px">
  <h4>Company</h4>
  <ul><li>Home</li><li>About Us</li><li>Why Us</li><li>Testimonials</li></ul>
</div>
<div class="abs foot-col" style="left:658px;top:2808px">
  <h4>Our Services</h4>
  <ul><li>Donec convallis pede</li><li>Aenenatis nibh</li><li>Duis quam Nam</li><li>Eget lacus</li><li>Aliquam erat</li></ul>
</div>
<div class="abs foot-col" style="left:883px;top:2808px">
  <h4>Resources</h4>
  <ul><li>Support</li><li>Sign Up</li><li>FAQ</li><li>Contact Us</li></ul>
</div>
<div class="abs foot-line"></div>
<div class="abs copy">© 2018 Company Name&nbsp; All right reserved&nbsp; Term of Use</div>

</body>
</html>
```